Compatible Printer Cartridge Box Design

We are looking to package toners cartridges & ink cartridges that we recycle in our shop. Attached is a doc file that tell what design we want, ideas, and sizes.

Unlike other compatible toner cartridges that are manufactured from scratch, LUMO Print Consumables are made from recycled original OEM print toners. This will maintain the original OEM parts inside the cartridge, maintain the original cartridge tolerance, ensure proper cartridge alignment in the printer, and minimize human error.

Project Deadline Extended
Reason: Hi to all, I am not satisfied with the current designs. I will extend for more 5 days and increase the budget. Thank You

Target Market(s)

Construction Companies, Banks, Hospitals, Oil Companies, Insurance Companies

Industry/Entity Type

Printer

Font styles to use
Other font styles liked:
• Calibri

Requirements
Must have
• The file must be in .ai format. So we can change the size of the box any time later.
• The file must be ready to be given to the printing press (specially the die cut). No any alteration must be made from our side.
• Since there are different models of cartridges, one side of the box must be left for a label that state the cartridge model, bar code, and compatible printers.
• The theme of the box must be quoted from our company logo, specially the colors. We prefer bold corporate design. Maybe with a woman on it (Not a must), and something related to protecting the environment. Avoid using the carton brown color.
• We prefer toner box that Can be opened from the top with that cartoon lock. For the ink cartridge, we would like to look like the zx one.
Nice to have
• Maybe with a woman on it (Not a must), and something related to protecting the environment.
Should not have
• Avoid using the carton brown color.

```html
<!DOCTYPE html>
<html lang="en">
<head>
<meta charset="utf-8">
<title>LUMO Premium Toner – Box Panels</title>
<link rel="stylesheet" href="https://fonts.googleapis.com/css2?family=Montserrat:wght@300;400;500;700&display=swap">
<style>
  :root {
    --bg-light: #d6d6d6;
    --bg-dark: #9a9a9a;
    --panel-white: #ffffff;
    --brand-orange: #e3871c;
    --brand-green: #8cb53f;
    --brand-gray: #58595b;
    --label-line: #9d9d9d;
    --badge-gray: #8a8b8d;
    --badge-gold: #d8a21f;
    --photo-warm: #f3b27a;
    --photo-red: #e2553a;
    --photo-teal: #3fb8a6;
    --photo-light: #f4efe6;
  }
  html, body {
    margin: 0;
    width: 1200px;
    height: 900px;
    overflow: hidden;
  }
  body {
    background: radial-gradient(ellipse at 50% 30%, var(--bg-light), var(--bg-dark));
    font-family: "Montserrat", sans-serif;
  }
  .box-dieline {
    display: block;
    width: 1200px;
    height: 900px;
  }
  .side-caption {
    font-family: "Montserrat", sans-serif;
    font-weight: 300;
    font-size: 22px;
    fill: #3f3f3f;
  }
  .brand-name {
    font-family: "Montserrat", sans-serif;
    font-weight: 500;
    fill: var(--brand-gray);
  }
  .brand-name--light { fill: var(--panel-white); }
  .product-line {
    font-family: "Montserrat", sans-serif;
    font-weight: 500;
    fill: var(--brand-gray);
  }
  .product-line--light { fill: var(--panel-white); }
  .tagline {
    font-family: "Montserrat", sans-serif;
    font-weight: 300;
    font-size: 25px;
    fill: var(--brand-gray);
  }
  .label-area-text {
    font-family: "Montserrat", sans-serif;
    font-weight: 400;
    font-size: 12px;
    fill: var(--brand-gray);
  }
  .company-address {
    font-family: "Montserrat", sans-serif;
    font-weight: 400;
    font-size: 5px;
    fill: var(--brand-gray);
  }
  .maker-name {
    font-family: "Montserrat", sans-serif;
    font-weight: 500;
    font-size: 7px;
    fill: var(--brand-gray);
  }
</style>
</head>
<body>
<svg class="box-dieline" viewBox="118 356 970 727.5" xmlns="http://www.w3.org/2000/svg">
  <defs>
    <linearGradient id="photo-tones" x1="0" y1="0" x2="1" y2="1">
      <stop offset="0" stop-color="var(--photo-warm)"/>
      <stop offset="0.35" stop-color="var(--photo-red)"/>
      <stop offset="0.6" stop-color="var(--photo-light)"/>
      <stop offset="1" stop-color="var(--photo-teal)"/>
    </linearGradient>
  </defs>

  <text class="side-caption" x="165" y="592">left side</text>
  <text class="side-caption" x="732" y="592">front side</text>
  <text class="side-caption" x="930" y="592">right side</text>

  <g class="panel panel--left">
    <rect x="128" y="608" width="177" height="254" fill="var(--panel-white)"/>
    <polygon points="305,775 305,862 250,862" fill="var(--brand-orange)"/>
    <rect class="label-area" x="145" y="625" width="148" height="165" rx="18" fill="none" stroke="var(--label-line)" stroke-width="1"/>
    <text class="label-area-text" x="219" y="702" text-anchor="middle">LABEL/STICKER</text>
    <text class="label-area-text" x="219" y="720" text-anchor="middle">AREA</text>
    <g class="company-address">
      <text x="146" y="808">Lumora Ink &amp; Printing Materials</text>
      <text x="146" y="815">48 Harbour Lane</text>
      <text x="146" y="822">Dubai, United Arab Emirates</text>
      <text x="146" y="829">PO Box 40210</text>
      <text x="146" y="836">Tel: +971 4 555 0142</text>
      <text x="146" y="843">hello@lumora-print.example</text>
      <text x="146" y="850">www.lumora-print.example</text>
    </g>
  </g>

  <g class="panel panel--front">
    <rect x="310" y="608" width="587" height="254" fill="var(--panel-white)"/>
    <polygon points="310,760 480,608 610,608 340,862 310,862" fill="var(--brand-orange)"/>
    <polygon points="610,608 790,608 560,862 340,862" fill="var(--brand-green)"/>
    <polygon role="img" aria-label="Photo: smiling woman holding a bunch of colourful balloons" points="760,608 897,608 897,862 690,862" fill="url(#photo-tones)"/>
    <text class="brand-name" x="340" y="697" font-size="46">LUMO</text>
    <text class="product-line" x="516" y="670" font-size="23">PREMIUM</text>
    <text class="product-line" x="516" y="694" font-size="23">TONER</text>
    <text class="tagline" x="600" y="822">Printing</text>
    <text class="tagline" x="600" y="852">Happy</text>
    <rect x="848" y="812" width="34" height="34" fill="var(--brand-orange)"/>
    <text class="maker-name" x="865" y="856" text-anchor="middle">Lumora</text>
  </g>

  <g class="panel panel--right">
    <rect x="902" y="608" width="176" height="254" fill="var(--panel-white)"/>
    <polygon points="902,608 1040,608 902,760" fill="var(--brand-orange)"/>
    <polygon points="1078,740 1078,862 965,862" fill="var(--brand-orange)"/>
    <text class="brand-name brand-name--light" x="912" y="644" font-size="25">LUMO</text>
    <text class="product-line product-line--light" x="912" y="663" font-size="9">PREMIUM</text>
    <text class="product-line product-line--light" x="912" y="673" font-size="9">TONER</text>
    <g class="certification-badges">
      <rect x="982" y="756" width="32" height="26" rx="3" fill="var(--badge-gray)"/>
      <rect x="912" y="788" width="30" height="24" rx="2" fill="var(--badge-gray)"/>
      <rect x="950" y="790" width="60" height="18" rx="2" fill="var(--badge-gray)"/>
      <circle cx="928" cy="835" r="14" fill="var(--badge-gold)"/>
      <circle cx="970" cy="835" r="14" fill="var(--badge-gold)"/>
    </g>
  </g>
</svg>
</body>
</html>
```